San Francisco Leading Consulting firm - 47Nova Web Design Project

•Create a Web Design
•Uncoded webpage layout design
•2 Pages Design - Homepage + Interior Page

Task Description
Hello, we're looking for a re-design our current website www.47nova-example.com

we have a sample mockup design @

http://47nova.civicpane-example.org/

This shows the layout that we like and also a sample of 6 pictures that would change based on where you mouse over..

6 pictures HOME design needs to be included.

SMART
THOUGHTFUL
FLEXIBLE
CREATIVE SERVICES
TECHNICAL SERVICES
PARTNERS

sites we like:

http://www.brelmoradvisory-example.com/Home.cfm?id=Home
http://www.pixelquarry-example.com/index.html

Our company can be best described as: 100+ employees, cutting-edge, depandable, innovative, strong, smart.

Our Primary focus is: IT Consulting Services and Creative Design services

47Nova LLC is a consulting firm providing creative design, business and technology solutions to both private and public interests.

Established in 1996, 47Nova is a San Francisco based company providing specialists for a range of business needs including:

Creative Design Services
•Print
•Logo Design
•Website Design
•Illustration

and

Business and Technology solutions

•Application Software and Web Development
•Business Process Re-Design (BPR)
•Business/Systems Analysis and Requirement Documentation
•Mentoring and Training
•Network/Hardware Installation Services
•System Design and Architecture
•Vendor Management
•Teamvault Architecture and Implementation

our sample mockup site:

Reason: Due to holiday season, we're not available to work with designers and finilize our design.  

Thank you very much for submitting your design.

We appreciate your time and creativity.   Since, our office is currently closed for holidays, we will be reviewing it in details next week and will make our decision as soon as possible.

It would be great if you could submit any of your changes by Wed next week, so it would be part of our reviews. 

Please see updated wireframe under attachments:  we have some minor updates to our wireframe that we would like you to update your designs, if possible.  

We also encorouge you not to use our standard wireframe and come up with more unique designs.   Everything would be considered when we review your design.

 

Target Market(s)

Creative services and professional services clients, including government agencies

Industry/Entity Type

Business

Requirements
Must have
• Clean, professional look, easy navigation

```html
<!DOCTYPE html>
<html lang="en">
<head>
<meta charset="utf-8">
<title>47Nova – Home</title>
<link rel="stylesheet" href="https://fonts.googleapis.com/css2?family=Didact+Gothic&family=Ubuntu:wght@500;700&family=Open+Sans:wght@400;600;700&display=swap">
<style>
:root{
  --page-top:#e9e9e9;
  --page-bottom:#ffffff;
  --panel:#ececec;
  --navy:#17456a;
  --navy-row:#1c5075;
  --blue-light:#4a95c8;
  --blue-head:#1a5a8c;
  --ink:#1b1b1b;
  --nav-ink:#222;
  --footer:#2c2c2c;
  --footer-text:#a8a8a8;
  --hatch-a:#d7d7d7;
  --hatch-b:#e6e6e6;
}
*{margin:0;padding:0;box-sizing:border-box}
html,body{width:1200px;height:892px;overflow:hidden}
body{position:relative;background:linear-gradient(var(--page-top),var(--page-bottom) 730px);font-family:"Open Sans",sans-serif;color:var(--ink)}
.abs{position:absolute}

.brand{left:187px;top:26px;display:flex;align-items:center;gap:12px}
.brand-dot{width:34px;height:34px;border-radius:50%;background:var(--blue-light)}
.brand-name{font-family:"Didact Gothic",sans-serif;font-size:34px;color:#555;letter-spacing:1px}

.main-nav{left:499px;top:48px;display:flex;align-items:center;font-family:"Didact Gothic",sans-serif;font-size:13.5px;color:var(--nav-ink)}
.main-nav a{color:inherit;text-decoration:none}
.main-nav .sep{margin:0 8px}
.main-nav .current{background:#dcdcdc;padding:4px 9px;margin-right:10px;color:#1a6aa8;font-weight:700;font-family:"Open Sans",sans-serif;font-size:14px}

.frame{left:177px;top:104px;width:846px;height:635px;background:repeating-linear-gradient(45deg,var(--hatch-a) 0 1px,var(--hatch-b) 1px 4px)}
.panel{left:187px;top:114px;width:826px;height:625px;background:linear-gradient(#ececec,#f1f1f1)}

.hero-art{left:419px;top:114px;width:593px;height:288px;background:linear-gradient(180deg,#2f78aa,#4c97c9 60%,#7bb4da)}
.hero-menu{left:188px;top:114px;width:231px;height:288px}
.hero-menu li{list-style:none;height:48px;background:var(--navy-row);border-bottom:1px solid #4c7b9d;display:flex;align-items:center;padding-left:10px;font-family:"Ubuntu",sans-serif;font-weight:700;font-size:20px;color:#fff}
.hero-menu li:first-child{background:var(--navy)}
.hero-menu li svg{margin-right:10px}
.hero-menu li.active{background:var(--navy);width:412px;justify-content:flex-start;padding-left:210px;font-size:25px}
.hero-copy{left:438px;top:310px;width:300px;font-family:"Open Sans",sans-serif;font-weight:600;font-size:10.6px;line-height:12.3px;color:#fff}
.hero-more{left:438px;top:382px;font-weight:700;font-size:10px;color:#fff;letter-spacing:.5px}

.feature{top:432px;width:236px}
.feature-title{height:31px;background:repeating-linear-gradient(45deg,#dadada 0 1px,#e4e4e4 1px 4px);text-align:center;font-family:"Ubuntu",sans-serif;font-weight:700;font-size:16px;line-height:31px;color:var(--blue-head)}
.feature-media{margin-top:5px;height:95px;background:#fff;border:1px solid #d4d4d4;padding:5px}
.feature-media div{width:100%;height:100%}
.feature h3{margin:16px 0 0 4px;font-size:11px;font-weight:700;letter-spacing:.3px}
.feature p{margin:6px 0 0 4px;font-size:10.5px;line-height:12.2px;width:222px}
.btn{display:block;margin-top:18px;width:104px;height:25px;border:1px solid #cfcfcf;border-radius:13px;background:linear-gradient(#fff,#e6e6e6);font-size:10.5px;font-weight:700;color:#444;line-height:23px;text-align:center}
.divider{top:437px;width:0;height:245px;border-left:1px dotted #b7b7b7}

.footer{left:0;top:739px;width:1200px;height:153px;background:var(--footer)}
.footer-frame{left:177px;top:739px;width:846px;height:153px;background:repeating-linear-gradient(45deg,#2f2f2f 0 1px,#353535 1px 4px)}
.footer-inner{left:187px;top:739px;width:826px;height:145px;background:var(--footer)}
.testimonial-title{left:192px;top:755px;font-family:"Ubuntu",sans-serif;font-weight:500;font-size:16px;color:#b8b8b8}
.testimonial-text{left:193px;top:782px;width:440px;font-size:10.6px;line-height:12px;color:var(--footer-text)}
.testimonial-name{left:194px;top:843px;font-size:10.5px;line-height:12px;color:var(--footer-text)}
.testimonial-name b{letter-spacing:.5px}
.testimonial-more{left:571px;top:843px;font-size:10px;font-weight:700;letter-spacing:.8px;color:var(--footer-text)}
.footer-rule{left:691px;top:764px;width:0;height:94px;border-left:1px solid #444}
.contact{right:203px;top:757px;text-align:right;font-size:10.6px;line-height:12px;color:var(--footer-text)}
.social{left:870px;top:824px;display:flex;gap:9px}
.social span{width:26px;height:26px;background:#8a8a8a;border-radius:3px}
.copyright{right:203px;top:855px;font-size:10.6px;color:var(--footer-text)}
</style>
</head>
<body>

<div class="abs brand"><span class="brand-dot"></span><span class="brand-name">47Nova</span></div>

<nav class="abs main-nav">
  <a class="current" href="#">Home</a>
  <a href="#">Company</a><span class="sep">|</span>
  <a href="#">Technical Services</a><span class="sep">|</span>
  <a href="#">Creative Services</a><span class="sep">|</span>
  <a href="#">Partners</a><span class="sep">|</span>
  <a href="#">Contact Us</a>
</nav>

<div class="abs frame"></div>
<div class="abs panel"></div>

<div class="abs hero-art" role="img" aria-label="Photo of a thoughtful woman with a thought bubble of question marks on a blue background"></div>

<ul class="abs hero-menu">
  <li><svg width="9" height="11" viewBox="0 0 9 11"><path d="M1 1l6 4.5L1 10" fill="none" stroke="#fff" stroke-width="2"/></svg>SMART</li>
  <li><svg width="9" height="11" viewBox="0 0 9 11"><path d="M1 1l6 4.5L1 10" fill="none" stroke="#fff" stroke-width="2"/></svg>FLEXIBLE</li>
  <li><svg width="9" height="11" viewBox="0 0 9 11"><path d="M1 1l6 4.5L1 10" fill="none" stroke="#fff" stroke-width="2"/></svg>CREATIVE SERVICES</li>
  <li class="active"><svg width="18" height="13" viewBox="0 0 18 13"><path d="M1 1l6 5.5L1 12M9 1l6 5.5L9 12" fill="none" stroke="#fff" stroke-width="2.4"/></svg>THOUGHTFUL</li>
  <li><svg width="9" height="11" viewBox="0 0 9 11"><path d="M1 1l6 4.5L1 10" fill="none" stroke="#fff" stroke-width="2"/></svg>TECHNICAL SERVICES</li>
  <li><svg width="9" height="11" viewBox="0 0 9 11"><path d="M1 1l6 4.5L1 10" fill="none" stroke="#fff" stroke-width="2"/></svg>PARTNERS</li>
</ul>

<p class="abs hero-copy">Lorem Ipsum is simply dummy text of the printing and typesetting industry. Lorem Ipsum has been the industry's standard dummy text ever since the 1500s, when an unknown printer took a galley of type and scrambled it.</p>
<span class="abs hero-more">Read More</span>

<section class="abs feature" style="left:201px">
  <div class="feature-title">FOR GRAPHIC DESIGNERS</div>
  <div class="feature-media"><div role="img" aria-label="Illustration of a head filled with gears" style="background:linear-gradient(90deg,#4a3f44,#a89040 60%,#4a3f44)"></div></div>
  <h3>Get Creative!</h3>
  <p>47Nova is looking for top creative talent to deliver graphic design solutions for some leading global brands Do you have what it takes?</p>
  <span class="btn">Read More</span>
</section>
<div class="abs divider" style="left:460px"></div>

<section class="abs feature" style="left:485px">
  <div class="feature-title">FOR CLIENTS</div>
  <div class="feature-media"><div role="img" aria-label="Photo of a glowing network globe" style="background:linear-gradient(100deg,#1a3a2c,#3f8f78 45%,#2d7fc0 75%,#061022)"></div></div>
  <h3>The 47Nova Difference</h3>
  <p>47Nova is looking for top creative talent to deliver graphic design solutions for some leading global brands Do you have what it takes?</p>
  <span class="btn">Read More</span>
</section>
<div class="abs divider" style="left:741px"></div>

<section class="abs feature" style="left:765px">
  <div class="feature-title">FOR PARTNERS</div>
  <div class="feature-media"><div role="img" aria-label="Photo of team members stacking hands together" style="background:linear-gradient(90deg,#b88068,#e6c4ad 50%,#c99278)"></div></div>
  <h3>Team Up With the Best</h3>
  <p>47Nova is looking for top creative talent to deliver graphic design solutions for some leading global brands Do you have what it takes?</p>
  <span class="btn">Read More</span>
</section>

<footer>
  <div class="abs footer"></div>
  <div class="abs footer-frame"></div>
  <div class="abs footer-inner"></div>
  <h2 class="abs testimonial-title">Testimonials</h2>
  <p class="abs testimonial-text">Now we can start to reap the benefits of current technology, including full vendor support, enhanced financial system functionality, and automation of manual processes. This upgrade was a necessary prerequisite to our full deployment of a strategic systems architecture.....</p>
  <p class="abs testimonial-name"><b>Dana Whitcombe</b><br>Director – IS, Harbor Authority of Bayside</p>
  <span class="abs testimonial-more">Read More</span>
  <div class="abs footer-rule"></div>
  <address class="abs contact" style="font-style:normal">47Nova, LLC<br>820 Larkmoor Avenue, Suite 410<br>San Francisco, CA 94199<br>Phone: 1-415-555-0142<br>Fax: 1-415-555-0147</address>
  <div class="abs social" aria-label="Social links"><span></span><span></span><span></span><span></span></div>
  <p class="abs copyright">Copyright 2010, 47Nova, LLC All rights reserved</p>
</footer>

</body>
</html>
```